Bright Fern Accounting Postcard

I need a postcard that highlights my services and contact info. Please use the website for graphics/info... www.BrightFernAccounting.example

Target Market(s)

Business owners

Industry/Entity Type

Bookkeeper

Colors

Designer to choose colors to be used in the design.

Requirements
Must have
• Services listed, Certified Tallyfox Cloud Elite Partner (can add Tallyfox logo), Contact info

```html
<!DOCTYPE html>
<html lang="en">
<head>
<meta charset="utf-8">
<title>Bright Fern Accounting Postcard</title>
<link rel="stylesheet" href="https://fonts.googleapis.com/css2?family=Montserrat:wght@500;600;800;900&family=Merriweather:wght@700&family=Oswald:wght@400;500&family=Roboto+Condensed:wght@400&display=swap">
<style>
  :root {
    --board: #434343;
    --navy: #1a2f5c;
    --navy-deep: #15295a;
    --band-blue: rgba(52, 84, 160, 0.82);
    --sky-top: #e7ebf2;
    --glass-blue: #3f5e9e;
    --glass-deep: #253e78;
    --window-glow: rgba(232, 186, 120, 0.55);
    --panel: #f1f2f4;
    --ink: #222;
    --heading: #1d3466;
    --green: #2ca01c;
    --white: #fff;
    --stamp: #b0b0b0;
    --rule: #222;
  }
  * { margin: 0; padding: 0; box-sizing: border-box; }
  html, body { width: 1200px; height: 1200px; overflow: hidden; background: var(--board); }
  .board { position: relative; width: 1200px; height: 1200px; }

  /* Front */
  .front { position: absolute; left: 130px; top: 137px; width: 603px; height: 466px; background: var(--navy); overflow: hidden; }
  .front__photo { position: absolute; left: 0; right: 0; top: 0; height: 340px;
    background:
      radial-gradient(ellipse 22% 30% at 52% 68%, var(--window-glow), transparent 70%),
      radial-gradient(ellipse 18% 26% at 80% 62%, rgba(232, 186, 120, 0.35), transparent 70%),
      radial-gradient(ellipse 16% 28% at 14% 55%, rgba(232, 186, 120, 0.3), transparent 70%),
      radial-gradient(ellipse 14% 40% at 40% 30%, rgba(220, 228, 240, 0.55), transparent 75%),
      linear-gradient(90deg, var(--glass-deep) 0%, var(--glass-blue) 30%, #52689a 45%, var(--glass-blue) 65%, #6d7fa8 100%); }
  .front__photo::after { content: ""; position: absolute; inset: 0;
    background: linear-gradient(180deg, rgba(231,235,242,0.85) 0%, rgba(231,235,242,0) 14%, rgba(26,47,92,0) 72%, var(--navy) 100%); }
  .front__band { position: absolute; left: 0; right: 0; top: 39px; height: 68px; background: var(--band-blue);
    display: flex; align-items: center; justify-content: center; gap: 10px; }
  .brand-mark { width: 22px; height: 22px; background: var(--white); }
  .brand-name { font-family: "Merriweather", serif; font-weight: 700; font-size: 27px; color: var(--white); letter-spacing: .3px; }
  .headline { position: absolute; left: 44px; top: 329px; font-family: "Montserrat", sans-serif; color: var(--white); line-height: 36px; }
  .headline__top { font-weight: 800; font-size: 35px; display: block; }
  .headline__bottom { font-weight: 500; font-size: 35px; letter-spacing: 1px; display: block; }
  .headline-frame { position: absolute; left: 0; top: 0; }
  .partner-badge { position: absolute; left: 508px; top: 348px; width: 44px; height: 44px; border-radius: 50%; background: var(--green); }
  .front__tagline { position: absolute; left: 21px; top: 408px; width: 575px; font-family: "Oswald", sans-serif; font-weight: 500;
    font-size: 15px; line-height: 19px; color: var(--white); letter-spacing: .3px; }

  /* Back */
  .back { position: absolute; left: 488px; top: 642px; width: 601px; height: 466px; background: var(--white); overflow: hidden; }
  .back__services { position: absolute; left: 0; top: 0; width: 326px; height: 466px; background: var(--panel); }
  .services-tab { position: absolute; left: 0; top: 16px; width: 162px; height: 23px; background: var(--navy-deep);
    clip-path: polygon(0 0, 100% 0, 97% 100%, 0 100%); font-family: "Montserrat", sans-serif; font-weight: 900; font-size: 19px;
    color: var(--white); line-height: 23px; padding-left: 16px; }
  .service { position: absolute; left: 66px; width: 250px; }
  .service__title { font-family: "Montserrat", sans-serif; font-weight: 600; font-size: 14.5px; color: var(--heading); letter-spacing: .4px; margin-bottom: 3px; }
  .service__text { font-family: "Roboto Condensed", sans-serif; font-size: 10px; line-height: 12px; color: var(--ink); }
  .service--bookkeeping { top: 42px; }
  .service--reporting { top: 135px; }
  .service--payroll { top: 229px; left: 64px; }
  .service-icon { position: absolute; }
  .team-photo { position: absolute; left: 8px; top: 306px; width: 304px; height: 112px;
    background: linear-gradient(180deg, var(--panel) 0%, #c9c3bb 40%, #8d857c 70%, #2c2c33 100%); }
  .contact-band { position: absolute; left: 0; top: 418px; width: 326px; height: 48px; background: var(--navy-deep);
    clip-path: polygon(0 0, 93% 0, 100% 100%, 0 100%); font-family: "Oswald", sans-serif; font-weight: 500; font-size: 12.5px;
    color: var(--white); line-height: 48px; padding-left: 22px; letter-spacing: .2px; white-space: nowrap; }
  .mail-side__brand { position: absolute; left: 338px; top: 25px; display: flex; align-items: center; gap: 3px; }
  .mail-side__brand .brand-mark { width: 9px; height: 9px; background: var(--navy); }
  .mail-side__brand .brand-name { font-size: 6.5px; color: var(--navy); letter-spacing: 0; }
  .stamp-box { position: absolute; left: 539px; top: 16px; width: 42px; height: 38px; background: var(--stamp); }
  .address-line { position: absolute; left: 387px; width: 183px; height: 1.5px; background: var(--rule); }
</style>
</head>
<body>
<div class="board">

  <section class="front">
    <div class="front__photo" role="img" aria-label="Photo of modern glass office towers with lit windows at dusk"></div>
    <div class="front__band">
      <span class="brand-mark"></span>
      <span class="brand-name">Bright Fern Accounting</span>
    </div>
    <svg class="headline-frame" width="603" height="466" aria-hidden="true">
      <polyline points="254,345 462,345 462,393 416,393" fill="none" stroke="#fff" stroke-width="1.2"/>
    </svg>
    <h1 class="headline">
      <span class="headline__top">BOUTIQUE</span>
      <span class="headline__bottom">ACCOUNTING FIRM</span>
    </h1>
    <div class="partner-badge" aria-label="Tallyfox partner badge"></div>
    <p class="front__tagline">Our Tallyfox Cloud Certified Professionals have the Knowledge and Expertise to Ensure<br>Professional, Accurate, High Quality Service.</p>
  </section>

  <section class="back">
    <div class="back__services">
      <div class="services-tab">Our Services</div>

      <svg class="service-icon" style="left:20px;top:62px" width="40" height="40" viewBox="0 0 40 40" aria-hidden="true">
        <ellipse cx="20" cy="30" rx="18" ry="6" fill="#1d3466"/>
        <ellipse cx="20" cy="22" rx="18" ry="6" fill="#1d3466" stroke="#f1f2f4" stroke-width="1.5"/>
        <ellipse cx="20" cy="12" rx="18" ry="8" fill="#1d3466" stroke="#f1f2f4" stroke-width="1.5"/>
        <text x="20" y="16" text-anchor="middle" font-family="Montserrat, sans-serif" font-weight="800" font-size="11" fill="#fff">$</text>
      </svg>
      <div class="service service--bookkeeping">
        <h2 class="service__title">BOOKKEEPING</h2>
        <p class="service__text">Let us take over the day to day bookkeeping so you can get back to running your business. We offer Tallyfox Cloud setup and ongoing bookkeeping, including daily journal entries, accounts payables &amp; receivables, bill pay, sales tax reporting &amp; payments, account reconciliation, and more.</p>
      </div>

      <svg class="service-icon" style="left:20px;top:160px" width="38" height="44" viewBox="0 0 38 44" aria-hidden="true" fill="none" stroke="#1d3466" stroke-width="1.4">
        <rect x="8" y="2" width="28" height="38"/>
        <rect x="20" y="7" width="12" height="10"/>
        <line x1="20" y1="12" x2="32" y2="12"/>
        <rect x="2" y="18" width="4" height="10"/><rect x="8" y="14" width="4" height="14"/>
        <line x1="12" y1="24" x2="32" y2="24"/><line x1="12" y1="29" x2="32" y2="29"/><line x1="12" y1="34" x2="32" y2="34"/>
      </svg>
      <div class="service service--reporting">
        <h2 class="service__title">FINANCIAL REPORTING</h2>
        <p class="service__text">We'll provide easy to understand financial reports that allow you and your team to manage cash flow, create budgets and make forecasting decisions. Want real time data? Let us provide solutions with the latest in mobile apps and dashboards.</p>
      </div>

      <svg class="service-icon" style="left:15px;top:248px" width="42" height="46" viewBox="0 0 42 46" aria-hidden="true" fill="none" stroke="#1d3466" stroke-width="1.6">
        <circle cx="8" cy="6" r="4"/><circle cx="21" cy="5" r="4"/><circle cx="34" cy="6" r="4"/>
        <rect x="6" y="16" width="30" height="10" rx="3"/>
        <path d="M4 14v20h8M38 14v20h-8M14 26v18M28 26v18"/>
      </svg>
      <div class="service service--payroll">
        <h2 class="service__title">PAYROLL PROCESSING</h2>
        <p class="service__text">Whether you have 5 employees or 100+, payroll can be an overwhelming and time consuming task. We offer full service payroll processing, including employee on boarding and reporting.</p>
      </div>

      <div class="team-photo" role="img" aria-label="Photo of a smiling team of business professionals"></div>
      <div class="contact-band">1.800.555.0142 | www.brightfernaccounting.example</div>
    </div>

    <div class="mail-side__brand">
      <span class="brand-mark"></span>
      <span class="brand-name">Bright Fern Accounting</span>
    </div>
    <div class="stamp-box" aria-label="Postage area"></div>
    <div class="address-line" style="top:227px"></div>
    <div class="address-line" style="top:254px"></div>
    <div class="address-line" style="top:282px"></div>
  </section>

</div>
</body>
</html>
```